Word Document Estimate Sheet

Good evening. I have an home renovations company that does a lot of estimates through word documents and then emailed them a PDF document. ArtHarbor did my logo and stationary projects and did a great job with it. Now I need my word document estimate sheet to be more standardized meaning sometimes my headers and footers move when I get to the bottom of the page , this make me have to do a copy and paste many times to put them back in their place also I have headings like Master Bedroom, Master Bath . I would like for them to always be bold, underlined and colon on the end now I always have to do this. I would like for the header and footers to not move when I get to the bottom of the page. Basically I want the same document with the same look as the document I send but with less retyping and copy and pasting. Hopefully this makes sense and you can help my estimates go faster.

Thanks,
Glen

Target Market(s)

Customer who want an estimate

Industry/Entity Type

It Company

Requirements
Must have
• 1.Must have same header and footer as the document I sent but want text to be standard.
• 2.Header and footer must not move when I get to the bottom of page.
• 3.Categories like Master Bedroom, Kitchen Area categories must already be in the document and if I want to delete them I can.
Nice to have
• I would love my estimate time to be cut in half because new word estimate sheet is simple to work with.
Should not have
• Don't change the header and footer design at all just make sure it doesn't move when I type.

```html
<!DOCTYPE html>
<html lang="en">
<head>
<meta charset="utf-8">
<title>Harlow Home Renovations – Estimate Sheet</title>
<link rel="stylesheet" href="https://fonts.googleapis.com/css2?family=Tinos:wght@400;700&display=swap">
<style>
  :root {
    --navy: #1f1d5a;
    --navy-deep: #1a1850;
    --header-grey: #e9e9ec;
    --section-grey: #e3e3e5;
    --ink: #1a1a1a;
    --paper: #ffffff;
    --footer-text: #ffffff;
  }
  html, body {
    margin: 0;
    padding: 0;
    width: 849px;
    height: 1200px;
    overflow: hidden;
    background: var(--paper);
  }
  .sheet {
    position: relative;
    width: 849px;
    height: 1200px;
    font-family: "Tinos", "Times New Roman", serif;
    color: var(--ink);
    background: var(--paper);
    overflow: hidden;
  }
  .letterhead {
    position: absolute;
    top: 0; left: 0;
    width: 100%;
    height: 106px;
    background: var(--header-grey);
    display: flex;
    align-items: center;
    justify-content: center;
  }
  .brand {
    display: flex;
    align-items: center;
    gap: 10px;
  }
  .brand-mark {
    width: 14px;
    height: 14px;
    border-radius: 50%;
    background: var(--navy);
  }
  .brand-name {
    font-size: 24px;
    font-weight: 700;
    color: var(--navy);
    letter-spacing: 0.5px;
  }
  .header-rule {
    position: absolute;
    top: 106px; left: 0;
    width: 100%;
    height: 8px;
    background: var(--navy);
    border-bottom: 3px solid var(--header-grey);
  }
  .estimate {
    position: absolute;
    top: 170px;
    left: 48px;
    width: 752px;
  }
  .room {
    margin: 0 0 90px 0;
  }
  .room-title {
    margin: 0;
    height: 37px;
    line-height: 37px;
    padding-left: 10px;
    background: var(--section-grey);
    font-size: 21px;
    font-weight: 700;
  }
  .room-items {
    margin: 10px 0 0 0;
    padding-left: 56px;
    font-size: 18px;
    min-height: 22px;
  }
  .room-items li { height: 22px; }
  .letterfoot {
    position: absolute;
    left: 0; bottom: 0;
    width: 100%;
    height: 130px;
    background: var(--navy-deep);
    color: var(--footer-text);
    text-align: center;
    font-size: 11.5px;
    line-height: 17px;
    box-sizing: border-box;
    padding-top: 36px;
  }
  .letterfoot .web { font-weight: 700; font-size: 12.5px; }
  .letterfoot p { margin: 0; }
</style>
</head>
<body>
<div class="sheet">
  <header class="letterhead">
    <div class="brand">
      <span class="brand-mark"></span>
      <span class="brand-name">Harlow Home Renovations</span>
    </div>
  </header>
  <div class="header-rule"></div>

  <main class="estimate">
    <section class="room">
      <h2 class="room-title">Master Bedroom:</h2>
      <ul class="room-items"><li></li></ul>
    </section>
    <section class="room">
      <h2 class="room-title">Master Bathroom:</h2>
      <ul class="room-items"><li></li></ul>
    </section>
    <section class="room">
      <h2 class="room-title">Bedroom #2:</h2>
      <ul class="room-items"><li></li></ul>
    </section>
    <section class="room">
      <h2 class="room-title">Bedroom #3:</h2>
      <ul class="room-items"><li></li></ul>
    </section>
    <section class="room">
      <h2 class="room-title">Kitchen Area:</h2>
      <ul class="room-items"><li></li></ul>
    </section>
  </main>

  <footer class="letterfoot">
    <p class="web">www.harlowhomerenovations.com</p>
    <p>Dana Harlow Office: 704-555-0147 &nbsp;|&nbsp; Glen Harlow Cell: 704-555-0146 &nbsp;|&nbsp; E-Mail: glen@harlowhomerenovations.com</p>
    <p>412 Oak Ridge Ave., Suite 20 Fairview, NC 28000</p>
  </footer>
</div>
</body>
</html>
```